Velmora Trade Group, Inc

We need a business design for Velmora Trade Group.

Industry/Entity Type

Business Management

Contact Information for Business Card

High end sharp look

Requirements
Must have
• Gold and White.
• Office address - 27118 4th Ave S. Ste B6 Harlow Bay, ND 58974
• Phone - 701.555.0148
• Office - 701.555.0172
• Email - Len@velmoratradegroup.example
Nice to have
• Clean and elegant look. We like to add the foil look on the business card
Should not have
• Randon colors

```html
<!DOCTYPE html>
<html lang="en">
<head>
<meta charset="utf-8">
<title>Velmora Trade Group – Business Card</title>
<link rel="stylesheet" href="https://fonts.googleapis.com/css2?family=Cinzel:wght@400&family=Open+Sans:wght@400;700&display=swap">
<style>
  :root {
    --backdrop: #8b8c8b;
    --card: #232323;
    --white: #f4f4f2;
    --gold: #e2bd45;
    --rule: #e8e8e6;
  }
  * { margin: 0; padding: 0; box-sizing: border-box; }
  html, body { width: 1200px; height: 781px; overflow: hidden; }
  body { background: var(--backdrop); position: relative; font-family: "Open Sans", Arial, sans-serif; }

  .card {
    position: absolute;
    left: 357px;
    width: 454px;
    height: 252px;
    background: var(--card);
  }
  .card--front { top: 102px; }
  .card--back { top: 409px; }

  .wordmark {
    position: absolute;
    font-family: "Cinzel", Georgia, serif;
    font-weight: 400;
    text-align: center;
    text-transform: uppercase;
    line-height: 1;
  }
  .wordmark__main, .wordmark__sub { display: block; white-space: nowrap; }
  .wordmark__rule { display: block; margin: 0 auto; }

  .card--front .wordmark { left: 29px; top: 31px; width: 164px; color: var(--white); }
  .card--front .wordmark__main { font-size: 29px; letter-spacing: 0; }
  .card--front .wordmark__sub { font-size: 12.5px; letter-spacing: 4.4px; margin-top: 7px; margin-right: -4.4px; }
  .card--front .wordmark__rule { width: 164px; height: 6px; margin-top: 4px; }

  .card--back .wordmark { left: 0; right: 0; top: 86px; color: var(--gold); }
  .card--back .wordmark__main { font-size: 39px; letter-spacing: 0.5px; }
  .card--back .wordmark__sub { font-size: 17px; letter-spacing: 6px; margin-top: 9px; margin-right: -6px; }
  .card--back .wordmark__rule { width: 218px; height: 8px; margin-top: 6px; }

  .holder { position: absolute; right: 17px; top: 135px; text-align: right; }
  .holder__name { color: var(--gold); font-weight: 700; font-size: 13.5px; line-height: 18px; }
  .holder__title { color: var(--white); font-size: 11px; line-height: 15px; }

  .rule {
    position: absolute; left: 28px; right: 17px; top: 174px;
    height: 1.5px; background: var(--rule);
  }

  .address {
    position: absolute; left: 28px; top: 184px;
    color: var(--white); font-size: 11px; line-height: 15px; font-style: normal;
  }

  .divider {
    position: absolute; left: 153px; top: 184px;
    width: 1px; height: 44px; background: var(--rule);
  }

  .contacts {
    position: absolute; left: 162px; top: 184px; list-style: none;
    color: var(--white); font-size: 11px; line-height: 15px;
  }
  .contacts li { display: flex; align-items: center; gap: 4px; }
  .contacts svg { width: 10px; height: 10px; flex: none; }
</style>
</head>
<body>
  <section class="card card--front" aria-label="Card front">
    <div class="wordmark">
      <span class="wordmark__main">Velmora</span>
      <span class="wordmark__sub">Trade Group</span>
      <svg class="wordmark__rule" viewBox="0 0 164 6" aria-hidden="true"><line x1="0" y1="3" x2="74" y2="3" stroke="var(--white)" stroke-width="0.8"/><line x1="90" y1="3" x2="164" y2="3" stroke="var(--white)" stroke-width="0.8"/></svg>
    </div>

    <div class="holder">
      <p class="holder__name">Jordan Hale</p>
      <p class="holder__title">Manager &amp; CEO</p>
    </div>

    <div class="rule"></div>

    <address class="address">
      27118 4th Ave S. Ste B6<br>
      Harlow Bay, ND 58974
    </address>

    <div class="divider"></div>

    <ul class="contacts">
      <li>
        <svg viewBox="0 0 10 10" aria-hidden="true"><rect x="2.5" y="0.5" width="5" height="9" rx="0.8" fill="none" stroke="var(--gold)" stroke-width="1"/><line x1="4" y1="8" x2="6" y2="8" stroke="var(--gold)" stroke-width="0.8"/></svg>
        701.555.0148
      </li>
      <li>
        <svg viewBox="0 0 10 10" aria-hidden="true"><path d="M2 1 L3.8 1 L4.4 3 L3.3 3.9 Q4.3 5.9 6.1 6.7 L7 5.6 L9 6.2 L9 8 Q8.5 9 7.5 9 Q1 8.3 1 2 Q1 1 2 1 Z" fill="var(--gold)"/></svg>
        701.555.0172
      </li>
      <li>
        <svg viewBox="0 0 10 10" aria-hidden="true"><path d="M0.5 3.5 L5 0.8 L9.5 3.5 L9.5 9 L0.5 9 Z" fill="var(--gold)"/><path d="M0.8 3.8 L5 6.6 L9.2 3.8" fill="none" stroke="var(--card)" stroke-width="0.8"/></svg>
        Len@velmoratradegroup.example
      </li>
    </ul>
  </section>

  <section class="card card--back" aria-label="Card back">
    <div class="wordmark">
      <span class="wordmark__main">Velmora</span>
      <span class="wordmark__sub">Trade Group</span>
      <svg class="wordmark__rule" viewBox="0 0 218 8" aria-hidden="true"><line x1="0" y1="4" x2="99" y2="4" stroke="var(--gold)" stroke-width="1"/><line x1="119" y1="4" x2="218" y2="4" stroke="var(--gold)" stroke-width="1"/></svg>
    </div>
  </section>
</body>
</html>
```